Vireo Tooling Company Website

We need a corporate logo and website design. The website will be built in Word Press, so the design should be able to be easily cut up to work within wordpress.

Vireo Tooling Company is a precision machine shop, which provides CNC Milling and CNC Turning as our two most popular services. Additionally, we provide prototyping services, including 3D CAD (designing) and mechanical engineering.

Our goal with the website is to get as many leads as possible. There is zero ecommerce, its strictly a lead generation campaign. The perfect website design would be a handful of pages which work almost like a squeeze page directing the website visitor to fill out a contact form and upload their project to our website's lead generation forms.

I've uploaded a few images of our work to give you and idea of what we do. Also, we already have a few domains, www.vireotoolingco.example and www.keldantooling.example for you to review. These websites suck, which is why we're looking for a new design.

Target Market(s)

Mechanical Engineers are our primary customer. Mostly males. Other customers are OEMs (equipment manufacturers in various industries and sectors)

Industry/Entity Type

Mechanical Engineering

Requirements
Must have
• We like the color green. Design should be sharp, clean, can have rounded edges, infact that's preferred, but not chunky and clunky. We are a precision machine shop so sharp fine edges are important.

social sharing on the website
Should not have
• should not be chunky and clunky

```html
<!DOCTYPE html>
<html lang="en">
<head>
<meta charset="utf-8">
<title>Vireo Tooling Company</title>
<link rel="stylesheet" href="https://fonts.googleapis.com/css2?family=Arimo:wght@400;700&display=swap">
<style>
:root{
  --green:#08a512;
  --green-dark:#067d0d;
  --text:#333333;
  --white:#ffffff;
  --grey-button:#9e9e9e;
  --footer-bg:#dedede;
}
*{margin:0;padding:0;box-sizing:border-box}
html,body{width:1200px;height:1000px;overflow:hidden}
body{font-family:"Arimo",Arial,sans-serif;color:var(--text);background:var(--white);position:relative}
.site-header{position:absolute;left:0;top:0;width:1200px;height:230px;
  background:linear-gradient(100deg,#dcdcdc 0%,#f1f1f1 35%,#e2e2e2 60%,#f3f3f3 80%,#d9d9d9 100%)}
.brand{position:absolute;left:124px;top:96px;display:flex;align-items:center;gap:14px}
.brand-square{width:28px;height:28px;background:var(--green);display:block}
.brand-name{font-weight:700;font-size:36px;color:var(--green);letter-spacing:-0.5px;line-height:40px}
.header-phone{position:absolute;right:109px;top:111px;font-size:18px;color:var(--green)}
.header-phone b{font-weight:700}
.account-links{position:absolute;top:151px;left:902px;display:flex;gap:24px}
.btn{display:block;height:20px;line-height:20px;font-size:12px;color:var(--white);border-radius:2px;text-align:center}
.btn-login{width:82px;background:var(--green);font-weight:700}
.btn-register{width:84px;background:var(--grey-button)}
.main-nav{position:absolute;left:0;top:230px;width:1200px;height:37px;background:var(--green);border-top:3px solid var(--green-dark)}
.main-nav ul{list-style:none;display:flex;position:absolute;left:125px;top:2px}
.main-nav li{font-size:18px;font-weight:700;color:var(--white);height:32px;line-height:30px;padding:0 10.5px;letter-spacing:0.2px}
.main-nav li.current{background:var(--white);color:var(--green);padding:0 8px}
.content{position:absolute;left:0;top:267px;width:825px;height:513px;background:var(--white)}
.sidebar{position:absolute;left:825px;top:267px;width:375px;height:513px;
  background:linear-gradient(90deg,#d3d3d3,#e6e6e6 50%,#d6d6d6)}
.welcome{position:absolute;left:127px;top:366px;width:660px}
.welcome h1{font-size:25px;color:var(--green);font-weight:700;margin-bottom:17px}
.welcome p{font-size:17px;line-height:19px;margin-bottom:19px}
.service-card{position:absolute;left:930px;width:163px}
.service-photo{height:96px}
.service-label{height:26px;background:var(--green);color:var(--white);font-weight:700;font-size:16px;text-align:center;line-height:26px;border-radius:0 0 2px 2px}
.feature-band{position:absolute;left:0;top:780px;width:1200px;height:182px;
  background:linear-gradient(90deg,#1c1c1c,#2a2a2a 50%,#1e1e1e)}
.feature-text{position:absolute;left:489px;top:800px;color:var(--white)}
.feature-text h2{font-size:25px;font-weight:700;margin-bottom:4px}
.feature-text p{font-size:17px;line-height:25px}
.feature-visual{position:absolute;left:127px;top:657px;width:355px;height:290px;
  background:linear-gradient(135deg,#0f3f6a 0%,#a9b4bf 35%,#dfe3e7 60%,#5b6570 100%);border-radius:4px}
.site-footer{position:absolute;left:0;top:962px;width:1200px;height:38px;background:var(--footer-bg);border-top:3px solid #bcbcbc}
.social{position:absolute;left:129px;top:10px;display:flex;gap:16px}
.social span{width:22px;height:22px;background:var(--green);border-radius:2px;display:block}
.footer-phone{position:absolute;right:103px;top:10px;font-size:18px;color:var(--text)}
.footer-phone b{font-weight:700}
</style>
</head>
<body>
<header class="site-header">
  <div class="brand"><span class="brand-square"></span><span class="brand-name">Vireo Tooling Company</span></div>
  <div class="header-phone">Call Us Now <b>(555)014-2290</b></div>
  <div class="account-links"><a class="btn btn-login">Client Login</a><a class="btn btn-register">Register Here</a></div>
</header>
<nav class="main-nav">
  <ul>
    <li class="current">Home About</li>
    <li>Service Guaranty</li>
    <li>Milling</li>
    <li>Turning</li>
    <li>Other Services</li>
    <li>Contact</li>
  </ul>
</nav>
<main class="content"></main>
<aside class="sidebar"></aside>
<section class="welcome">
  <h1>Welcome!</h1>
  <p>Our business is dedicated to becoming one of your top suppliers and first choice<br>for quality, on-time, precision machining services. You'll receive unparalleled service<br>from Vireo Tooling Company because we work hard to make sure that we always<br>satisfy your needs. We are committed to deliver excellence in everything we do.</p>
  <p>We are committed to deliver excellence in everything we do. Our staff knows that<br>the only way we can continue being a successful business is by making you happy.<br>Feel confident that you are receiving exceptional products and services<br>by choosing <b>Vireo Tooling Company</b>.</p>
</section>
<div class="service-card" style="top:311px">
  <div class="service-photo" role="img" aria-label="Photo of assembly work with sparks" style="background:linear-gradient(135deg,#0c1c2c,#3b6f95 50%,#1a1a22)"></div>
  <div class="service-label">Assembly</div>
</div>
<div class="service-card" style="top:462px">
  <div class="service-photo" role="img" aria-label="Photo of a fabricated metal part in hand" style="background:linear-gradient(135deg,#5a3a22,#c9b9a0 50%,#6b4a33)"></div>
  <div class="service-label">Fabrication</div>
</div>
<div class="service-card" style="top:613px">
  <div class="service-photo" role="img" aria-label="Photo of a CNC machine cutting metal" style="background:linear-gradient(135deg,#4c5560,#c8d0d8 50%,#3a424a)"></div>
  <div class="service-label">Machining</div>
</div>
<section class="feature-band"></section>
<div class="feature-visual" role="img" aria-label="Illustration of a monitor showing CAD gears and bearings"></div>
<div class="feature-text">
  <h2>Much more than a normal machine shop</h2>
  <p>Use our full service design team to help you<br>create prototypes of your equipment.</p>
</div>
<footer class="site-footer">
  <div class="social" aria-label="Social links"><span></span><span></span><span></span><span></span></div>
  <div class="footer-phone">Call Us Now <b>(555)014-2290</b></div>
</footer>
</body>
</html>
```